2 Business Card Designs

Need two business cards designed:
1) for lumora studio (wedding video) website is lumorastudio.com.au
2) for lumora studio (corporate video) website is lumorastudio.net.au

I am looking for something simple, no fancy shapes etc. Just elegant, simple and classy.

Both companies are video companies, one specialising in weddings the other corporate videos. Neither card needs to have any pics of video or camera related images. Please use same colour schemes as respective websites.

Logo is the same but can change colour.

Industry/Entity Type

Camera

Requirements
Must have
• Logo should be either all white or a colour to match websites
Should not have
• swirls, flowers, shapes, etc.

```html
<!DOCTYPE html>
<html lang="en">
<head>
<meta charset="utf-8">
<title>Lumora Studio Business Cards</title>
<link rel="stylesheet" href="https://fonts.googleapis.com/css2?family=Exo+2:wght@300;400&display=swap">
<style>
  :root {
    --backdrop: #e9e4df;
    --card-light: #ffffff;
    --card-dark: #474747;
    --ink-dark: #3f3f3f;
    --ink-mid: #555555;
    --ink-light: #a9a9a9;
    --ink-pale: #f1f1f1;
    --band: #474747;
  }
  * { margin: 0; padding: 0; box-sizing: border-box; }
  html, body {
    width: 1200px;
    height: 900px;
    overflow: hidden;
    background: var(--backdrop);
    font-family: "Exo 2", Arial, sans-serif;
  }
  .canvas {
    position: relative;
    width: 1200px;
    height: 900px;
  }
  .card {
    position: absolute;
    top: 324px;
    width: 530px;
    height: 303px;
    text-align: center;
    box-shadow: 0 2px 6px rgba(0,0,0,0.18);
  }
  .card--front { left: 37px; background: var(--card-light); }
  .card--back { left: 634px; background: var(--card-dark); }

  .brand-name {
    position: absolute;
    left: 0; right: 0;
    top: 56px;
    font-size: 50px;
    font-weight: 300;
    letter-spacing: 1px;
    line-height: 1;
  }
  .card--front .brand-name { color: var(--ink-dark); }
  .card--back .brand-name { color: var(--ink-light); }

  .brand-rule {
    position: absolute;
    left: 110px;
    top: 150px;
    width: 310px;
    height: 2px;
  }
  .card--front .brand-rule { background: linear-gradient(90deg, rgba(60,60,60,0), rgba(60,60,60,0.55), rgba(60,60,60,0)); }
  .card--back .brand-rule { background: linear-gradient(90deg, rgba(200,200,200,0), rgba(220,220,220,0.7), rgba(200,200,200,0)); }

  .holder-name {
    position: absolute;
    left: 0; right: 0;
    top: 176px;
    font-size: 24px;
    font-weight: 400;
    color: var(--ink-dark);
  }
  .contact-lines {
    position: absolute;
    left: 0; right: 0;
    top: 227px;
    font-size: 11px;
    line-height: 15px;
    color: var(--ink-mid);
  }
  .front-band {
    position: absolute;
    left: 0; right: 0; bottom: 0;
    height: 8px;
    background: var(--band);
  }

  .web-address {
    position: absolute;
    left: 0; right: 0;
    top: 175px;
    font-size: 16px;
    font-weight: 300;
    letter-spacing: 0.6px;
    color: var(--ink-pale);
  }
  .hours-lines {
    position: absolute;
    left: 0; right: 0;
    top: 230px;
    font-size: 12px;
    line-height: 15px;
    color: var(--ink-pale);
  }
</style>
</head>
<body>
<main class="canvas">
  <section class="card card--front" aria-label="Business card front">
    <h1 class="brand-name">lumora studio</h1>
    <div class="brand-rule"></div>
    <p class="holder-name">Owen Haldane</p>
    <p class="contact-lines">Marlow :: NSW :: 2090<br>Phone: +61 2 5550 1847</p>
    <div class="front-band"></div>
  </section>

  <section class="card card--back" aria-label="Business card back">
    <h2 class="brand-name">lumora studio</h2>
    <div class="brand-rule"></div>
    <p class="web-address">www.lumorastudio.net.au</p>
    <p class="hours-lines">Monday-Friday 9am-5pm<br>Evening Viewings available<br>All bookings via appointment only.318 Harbour Road</p>
  </section>
</main>
</body>
</html>
```